Tavner's Produce Business Cards

A new style and great looking business cards for my parents business. Simple yet catchy and something that shows a home grown produce and apples farm!

Target Market(s)

Farmers market buyers, someone who loves home grown produce, fresh vegetables and apples.

Industry/Entity Type

Business

Requirements
Must have
• Tavner's Produce is the name, so that will have to be on the card. Also incorporate our logo! but maybe not exactly the same? Open to all ideas!

Marisela Tavner ( Owner)

Address: 42 Cedar Hollow Ln.
Alder Bend, ZZ 00547

Phone: (555) 555-0147
Cell (555) 555-0183
Nice to have
• I have a logo that was done not too long ago using design! I would like to have parts of the logo be used, but I also want examples of NOT using the logo and see if we can get the family produce look too it!

```html
<!DOCTYPE html>
<html lang="en">
<head>
<meta charset="utf-8">
<title>Tavner's Produce Business Cards</title>
<link href="https://fonts.googleapis.com/css2?family=Jost:wght@400;500;700&display=swap" rel="stylesheet">
<style>
  :root {
    --bg: #e9e6e2;
    --green: #0a7a3d;
    --green-light: #138a47;
    --green-dark: #056a33;
    --red: #a3202a;
    --yellow: #f5e63a;
    --white: #ffffff;
    --ink: #231f20;
  }
  * { margin: 0; padding: 0; box-sizing: border-box; }
  html, body { width: 1200px; height: 900px; overflow: hidden; }
  body {
    background: var(--bg);
    font-family: "Jost", Arial, sans-serif;
    position: relative;
  }
  .card {
    position: absolute;
    top: 272px;
    width: 557px;
    height: 317px;
    border-radius: 14px;
    overflow: hidden;
    background: radial-gradient(ellipse at 45% 30%, var(--green-light) 0%, var(--green) 55%, var(--green-dark) 100%);
    box-shadow: 0 3px 10px rgba(0,0,0,0.25);
  }
  .card--front { left: 27px; }
  .card--back { left: 617px; }
  .card__shape { position: absolute; inset: 0; width: 100%; height: 100%; }
  .farm-scene {
    position: absolute;
    border-radius: 50% 50% 0 0;
    background: radial-gradient(ellipse at 50% 60%, rgba(120,190,130,0.28), rgba(120,190,130,0) 70%);
  }
  .card--front .farm-scene { left: 0; bottom: 0; width: 200px; height: 110px; }
  .card--back .farm-scene { left: 60px; bottom: 0; width: 440px; height: 160px; }
  .brand-mark {
    position: absolute;
    border-radius: 50%;
    background: var(--white);
    display: flex;
    align-items: center;
    justify-content: center;
    text-align: center;
    box-shadow: 0 2px 8px rgba(0,0,0,0.25);
  }
  .brand-mark__name {
    color: var(--green);
    font-weight: 700;
    line-height: 1.05;
  }
  .card--front .brand-mark { left: 37px; top: 66px; width: 184px; height: 184px; }
  .card--front .brand-mark__name { font-size: 30px; }
  .card--back .brand-mark { left: 152px; top: 45px; width: 226px; height: 226px; }
  .card--back .brand-mark__name { font-size: 37px; }
  .contact {
    position: absolute;
    left: 331px;
    top: 94px;
    color: var(--ink);
    font-size: 14.5px;
    line-height: 1.3;
  }
  .contact__name { font-size: 17.5px; font-weight: 700; }
  .contact__role { font-size: 13px; margin-bottom: 16px; }
  .contact__address { margin-bottom: 16px; }
</style>
</head>
<body>
  <section class="card card--front">
    <div class="farm-scene" role="img" aria-label="Faint illustration of a tractor in rolling fields"></div>
    <svg class="card__shape" viewBox="0 0 557 317" preserveAspectRatio="none" aria-hidden="true">
      <path d="M338 0 Q262 150 308 317 L557 317 L557 0 Z" fill="var(--red)"/>
      <path d="M352 0 Q280 150 320 317 L557 317 L557 0 Z" fill="var(--yellow)"/>
      <path d="M360 0 Q290 150 329 317 L557 317 L557 0 Z" fill="var(--white)"/>
    </svg>
    <div class="brand-mark"><span class="brand-mark__name">Tavner's<br>Produce</span></div>
    <div class="contact">
      <p class="contact__name">Marisela Tavner</p>
      <p class="contact__role">Owner</p>
      <p class="contact__address">Address: 42 Cedar Hollow Ln.<br>Alder Bend, ZZ 00547</p>
      <p class="contact__phone">Phone: (555) 555-0147<br>Cell (555) 555-0183</p>
    </div>
  </section>

  <section class="card card--back">
    <div class="farm-scene" role="img" aria-label="Faint illustration of a tractor, rising sun and rolling fields"></div>
    <div class="brand-mark"><span class="brand-mark__name">Tavner's<br>Produce</span></div>
  </section>
</body>
</html>
```